Coaching landingpage/salespage need a layout

Hi!
We are two people from Sweden looking for help to design our coaching landingpage/salespage.

What about:
We need a nice modern timeless appealing Photoshop layout (landingpage) for our coaching page where we coach people to “how to get a richer lifestyle”.

Style of page:
We want the site to reflect seriousness but still harmonic. We would like somewhat colorful and (but not too crazy). After all, we are coaching about investments and private economy.
Responsive layout – consider stacking order when scaling down window width. Fullpage-design where content areas are 960 grid/max-width.

----------------------------------------------------------------------------
Content on page:
*Headersection – Logo and header image with the two coaches together and space for later on adding a video.

*On the landingpage the customers can read up on what we mean by a richer lifestyle (use dummy text). We show our Vardagskartan (= Everyday chart) and a little description about that. If the customers want to know more, they can click "read more (or a symbolic icon that relates to read more)" to expand a hidden div (section) where they can read more about Vardagskartan. They can also minimize the section.

*3-4 Unique selling points “Four reasons why choose coaching” with nice designed number-icons and some place for text.

*The customer should also be able to read something about what happens during a typical coaching session, some bullets that summarize it (use dummy text) and a couple of headlines, maybe 3 or 4 (about what they need to prepare for themselves .eg Skype, headset/microphone etc).

*Offer/product section: A section where the customer can see what services we provide, choose product and click order. When customer click order they will arrive to an order-page (this one you don’t have to design) .
Our products are as followed: Bronze (single coaching session), Silver (small-package), Gold (large-package). Use provided graphics for these products.

*Testimonials section. Currently we have 2 good testimonials, but only with text no portrait picture.

Testimonial1: “Uppiggande och inspirerande! Kommer med enkla vardagstips såväl som svårare tips. Ett roligt sätt att få en spark i baken, så att ekonomi-energin bibehålls! Tack för ett bra samtal!" - Henrietta Bjurvik

Testimonial2: "Värdefullast för mig var kunskapen om alternativa investeringssställen som inte är börs eller eget ägande." - Evelina Dunberg

*Section with portraits and info about the coaches (currently 2 coaches, but in future will be several, so a design-section that’s lets us add more coaches).

*Footer-section
------------------------------------------------------------------------

Colors:
Use Vardagskartan (attached file) as colorinspiration. Doesn’t have to be exactly those colors, you can use similar colors if it is more pleasing to the eye and you can also use complementary colors.

Currently we have tried of our own but don't really nail it with any apealing design. This is what we have done so far but we want to replace it with your more professional design:

https://www.kolmsteg.se/full/Page/coaching13
-------------------------------------------------------------

SUMMARIZE of the above design-description:

* Our logo (attached psd-file with smart-object. You can try different colors with color-overlay)

*Apealing headerimage with portrait (attached file "big_portrait")

*Introduction text (use dummy text about 100 words)

*Text about Vardagskartan (use dummy text about 200 words)

*Vardagskartan (attached psd-file with smart-object)

*What we are covering during a coaching session (dummy text about 200 words and about 5 or 6 bullets)

*3-4 Unique Selling Points with stylish number icons (not 2 small) and some text.
*Our offers Bronze, Silver, Gold (attached pictures)
*Testimonials
*Picture & info about coaches (attached pictures, choose whichever suits you)
*Footer

Please comment if there are questions.

Reagards Torbjörn @ Kolm Steg

Target Market(s)

People who want to learn how to create a richer lifestyle which involves more freedom and a better well-being

Number of Pages Required

1 page

Font styles to use
Sans Serif
Other font styles liked:
• Roboto

Requirements
Should not have
• A cheezy unmodern landingpage with lots of texts and 10 sign-up buttons.
• This page is not a site about capturing emails and building lists by provide a "best-guide-for-something". It´s about getting people to book and pay for one or more coaching-sessions.

```html
<!DOCTYPE html>
<html lang="sv">
<head>
<meta charset="utf-8">
<title>Kolm Steg – Livsstilscoaching</title>
<link rel="stylesheet" href="https://fonts.googleapis.com/css2?family=Noto+Sans:wght@400;700&display=swap">
<style>
:root{
  --navy:#1b2f4e;
  --navy-deep:#14253f;
  --tab:#0f4a68;
  --cyan:#0e9ad8;
  --card:#0aa0dc;
  --pale:#e6f0fa;
  --panel:#f0f0f0;
  --red:#d9434f;
  --ink:#1e1e1e;
  --muted:#555;
  --link:#2fa8e6;
  --white:#fff;
}
*{box-sizing:border-box;margin:0;padding:0}
html,body{width:1200px;height:2937px;overflow:hidden}
body{font-family:"Noto Sans",Arial,sans-serif;color:var(--ink);background:var(--white);position:relative}
section,header,footer{position:absolute;left:0;width:1200px}
.tab{position:absolute;left:50%;transform:translateX(-50%);background:var(--tab);color:var(--white);
  font-size:19px;letter-spacing:.5px;padding:4px 44px;white-space:nowrap;
  clip-path:polygon(22px 0,calc(100% - 22px) 0,100% 100%,0 100%)}
.tab.flip{clip-path:polygon(0 0,100% 0,calc(100% - 22px) 100%,22px 100%)}

/* header */
.topbar{top:0;height:75px;background:var(--navy)}
.brand{position:absolute;left:195px;top:18px;display:flex;align-items:center;gap:12px;color:var(--white)}
.brand-dot{width:36px;height:36px;background:var(--white);border-radius:50%}
.brand-name{font-size:22px;letter-spacing:1px;line-height:1}
.brand-sub{font-size:14px;display:block;margin-top:3px}
.hero{top:75px;height:455px;background:radial-gradient(ellipse at 60% 40%,#3a8fe0 0%,#124a9c 45%,#0a2150 100%)}
.hero::after{content:"";position:absolute;left:0;right:0;top:0;height:6px;background:#d5dde8}
.hero-photo{position:absolute;left:370px;top:120px;width:480px;height:335px;
  background:linear-gradient(180deg,#6b7f9a 0%,#2e3442 70%,#22262f 100%);border-radius:160px 160px 0 0}
.hero-banner{position:absolute;left:291px;top:31px;width:657px;height:56px;background:var(--red);
  color:var(--white);font-size:17px;display:flex;align-items:center;justify-content:center}

.intro{top:482px;left:187px;width:820px;height:271px;background:var(--white);box-shadow:0 2px 8px rgba(0,0,0,.25)}
.intro .tab{top:0;font-size:22px}
.intro-text{position:absolute;top:48px;left:26px;right:26px;text-align:center;font-size:16px;line-height:22px}
.intro-text p+p{margin-top:22px}
.read-more{color:#999;font-style:italic;font-size:14px}
.read-more svg{vertical-align:middle;margin-left:4px}

/* reasons */
.reasons{top:777px;height:216px;background:var(--navy)}
.reasons .tab{top:0;font-size:16px}
.usp{position:absolute;top:49px;width:183px;height:138px;background:var(--card);color:var(--white)}
.usp svg{position:absolute;left:8px;top:14px}
.usp h3{position:absolute;left:77px;top:20px;font-size:12px}
.usp p{position:absolute;left:77px;top:40px;width:95px;font-size:11px;line-height:13px}
.usp .fold{position:absolute;right:0;bottom:0;width:32px;height:32px;
  background:linear-gradient(135deg,#d8d8d8 50%,var(--navy) 50%)}

/* sessions */
.sessions{top:993px;height:600px;background:var(--pale)}
.sessions .tab{top:0;font-size:19px}
.sessions-body{position:absolute;left:218px;width:770px;top:58px;font-size:16.5px;line-height:22px}
.bullets{list-style:none;margin:26px 0 16px 0}
.bullets li{position:relative;padding-left:30px;margin-bottom:13px}
.bullets li::before{content:"";position:absolute;left:0;top:5px;width:13px;height:13px;border-radius:50%;
  background:var(--red);box-shadow:2px 2px 0 #fff inset}
.sessions-body h4{font-size:17px;margin:0 0 16px 8px}
.sessions-body h4 ~ p{margin-bottom:16px}

/* services */
.services{top:1593px;height:496px}
.services .tab{top:0;font-size:19px}
.plans{position:absolute;left:183px;top:46px;width:824px;height:403px;background:var(--panel);display:flex}
.plan{flex:1;position:relative;text-align:center;border-right:1px solid #cfcfcf;margin:28px 0}
.plan:last-child{border-right:0}
.medal{width:170px;height:170px;border-radius:50%;margin:24px auto 0;box-shadow:0 10px 14px rgba(0,0,0,.15)}
.medal.bronze{background:radial-gradient(circle at 40% 35%,#f0a868,#c5702e 60%,#9a5320)}
.medal.silver{background:radial-gradient(circle at 40% 35%,#f2f2f2,#bdbdbd 60%,#8f8f8f)}
.medal.gold{background:radial-gradient(circle at 40% 35%,#fff08a,#f0c820 60%,#c79a10)}
.plan h3{font-size:17px;font-weight:400;margin-top:18px;line-height:20px}
.plan .kind{font-size:13px;display:block}
.plan p{font-size:13px;color:var(--muted);margin-top:12px}
.order{position:absolute;left:50%;transform:translateX(-50%);bottom:-4px;display:flex;align-items:center;
  background:var(--navy);color:var(--white);font-size:14px;height:34px;border-radius:17px;padding:0 18px 0 0}
.order-icon{width:42px;height:42px;border-radius:50%;background:var(--red);border:3px solid #fff;
  margin:0 10px 0 -6px;display:flex;align-items:center;justify-content:center}
.guarantee{position:absolute;top:462px;left:0;width:100%;text-align:center;font-size:11px}

/* testimonials */
.testimonials{top:2089px;height:134px;background:var(--cyan);color:var(--white)}
.testimonials .tab{top:0;font-size:19px}
.quote{position:absolute;top:50px;left:250px;width:700px;text-align:center;font-size:16.5px;line-height:21px}

/* coaches */
.coaches{top:2223px;height:436px;background:var(--pale)}
.coaches .tab{top:0;font-size:19px}
.coach{position:absolute;top:33px;width:300px;text-align:center}
.coach-photo{width:172px;height:158px;margin:0 auto;border-radius:18px;border:5px solid #fff;
  background:linear-gradient(180deg,#8c8f95,#3b3e45);box-shadow:0 2px 6px rgba(0,0,0,.25)}
.coach h3{font-size:17px;font-weight:400;margin-top:18px}
.coach .mail{font-size:16px}
.coach p{font-size:15.5px;line-height:20px;margin:46px auto 0;width:280px}
.divider{position:absolute;left:596px;top:160px;width:1px;height:200px;background:#c5cfd9}

/* footer */
.footer{top:2659px;height:278px;background:var(--navy-deep);color:var(--link)}
.footer .tab{top:0;font-size:19px}
.contact{position:absolute;left:218px;top:60px;font-size:16px;line-height:21px}
.contact .gap{margin-top:22px}
.follow{position:absolute;left:758px;top:60px;font-size:16px}
.social{position:absolute;left:896px;display:flex;align-items:center;gap:10px;font-size:14px;color:var(--white)}
.social span.dot{width:56px;height:56px;border-radius:50%;background:#3b7fc4;border:2px solid #fff}
.copyright{position:absolute;bottom:28px;width:100%;text-align:center;color:var(--white);font-size:16px}
</style>
</head>
<body>

<header class="topbar">
  <div class="brand">
    <span class="brand-dot"></span>
    <div><span class="brand-name">KOLM STEG</span><span class="brand-sub">LIVSSTILSCOACHING</span></div>
  </div>
</header>

<section class="hero">
  <div class="hero-photo" role="img" aria-label="Portrait of the two coaches standing together in front of a blue dewy web background"></div>
  <div class="hero-banner">Livsstilscoaching Lorem ipsum dolor sit amet, consectetuer adipiscing elit.</div>
</section>

<section class="intro">
  <div class="tab">WELCOME TO VARDAGSKARTAN</div>
  <div class="intro-text">
    <p>Livsstilscoaching Lorem ipsum dolor sit amet, consectetuer adipiscing elit. Aenean commodo ligula eget dolor. Aenean massa. Cum sociis natoque penatibus et magnis dis parturient montes, nascetur ridiculus mus. Donec quam felis, ultricies nec, pellentesque eu, pretium quis, sem. Nulla consequat massa quis enim.</p>
    <p>Donec pede justo, fringilla vel, aliquet nec, vulputate eget, arcu. In enim justo, rhoncus ut, imperdiet a, venenatis vitae, justo. Nullam dictum felis eu pede mollis pretium. Integer tincidunt. Cras dapibus. Vivamus elementum semper nisi. Aenean vulputate eleifend tellus. Aenean leo ligula, porttitor eu, consequat vitae, eleifend ac, enim. <span class="read-more">read more<svg width="18" height="16" viewBox="0 0 18 16"><path d="M1 1l7 7-7 7M9 1l7 7-7 7" fill="none" stroke="#e0572a" stroke-width="3"/></svg></span></p>
  </div>
</section>

<section class="reasons">
  <div class="tab flip">REASONS WHY CHOOSE COACHING</div>
  <div class="usp" style="left:185px">
    <svg width="64" height="86" viewBox="0 0 64 86"><path d="M32 84C32 84 4 50 4 30a28 28 0 0 1 56 0c0 20-28 54-28 54z" fill="#fff"/><circle cx="32" cy="30" r="20" fill="#1f86c8"/><text x="32" y="40" text-anchor="middle" font-size="28" font-style="italic" fill="#fff" font-family="Noto Sans,sans-serif">1</text></svg>
    <h3>Livsstilscoaching</h3><p>Lorem ipsum dolor sit amet, consectetuer adipiscing elit.</p><span class="fold"></span>
  </div>
  <div class="usp" style="left:397px">
    <svg width="64" height="86" viewBox="0 0 64 86"><path d="M32 84C32 84 4 50 4 30a28 28 0 0 1 56 0c0 20-28 54-28 54z" fill="#fff"/><circle cx="32" cy="30" r="20" fill="#1f86c8"/><text x="32" y="40" text-anchor="middle" font-size="28" font-style="italic" fill="#fff" font-family="Noto Sans,sans-serif">2</text></svg>
    <h3>Livsstilscoaching</h3><p>Lorem ipsum dolor sit amet, consectetuer adipiscing elit.</p><span class="fold"></span>
  </div>
  <div class="usp" style="left:612px">
    <svg width="64" height="86" viewBox="0 0 64 86"><path d="M32 84C32 84 4 50 4 30a28 28 0 0 1 56 0c0 20-28 54-28 54z" fill="#fff"/><circle cx="32" cy="30" r="20" fill="#1f86c8"/><text x="32" y="40" text-anchor="middle" font-size="28" font-style="italic" fill="#fff" font-family="Noto Sans,sans-serif">3</text></svg>
    <h3>Livsstilscoaching</h3><p>Lorem ipsum dolor sit amet, consectetuer adipiscing elit.</p><span class="fold"></span>
  </div>
  <div class="usp" style="left:824px">
    <svg width="64" height="86" viewBox="0 0 64 86"><path d="M32 84C32 84 4 50 4 30a28 28 0 0 1 56 0c0 20-28 54-28 54z" fill="#fff"/><circle cx="32" cy="30" r="20" fill="#1f86c8"/><text x="32" y="40" text-anchor="middle" font-size="28" font-style="italic" fill="#fff" font-family="Noto Sans,sans-serif">4</text></svg>
    <h3>Livsstilscoaching</h3><p>Lorem ipsum dolor sit amet, consectetuer adipiscing elit.</p><span class="fold"></span>
  </div>
</section>

<section class="sessions">
  <div class="tab flip">OUR TYPICAL COACHING SESSIONS:</div>
  <div class="sessions-body">
    <p>Lorem ipsum dolor sit amet, consectetuer adipiscing elit. Aenean commodo ligula eget dolor. Aenean massa. Cum sociis natoque penatibus et magnis dis parturient montes, nascetur ridiculus mus. Donec quam felis, ultricies nec, pellentesque eu, pretium quis, sem. Nulla consequat massa quis enim. Donec pede justo, fringilla vel, aliquet nec, vulputate eget, arcu. In enim justo.</p>
    <ul class="bullets">
      <li>Lorem ipsum dolor sit amet, consectetuer adipiscing elit.</li>
      <li>Lorem ipsum dolor sit amet, consectetuer adipiscing elit.</li>
      <li>Lorem ipsum dolor sit amet, consectetuer adipiscing elit.</li>
      <li>Lorem ipsum dolor sit amet, consectetuer adipiscing elit.</li>
    </ul>
    <h4>DONEC PEDE JUSTO, FRINGILLA VEL?</h4>
    <p>aliquet nec, vulputate eget, arcu. In enim justo, rhoncus ut, imperdiet a, venenatis vitae, justo. Nullam dictum felis eu pede mollis pretium. Integer tincidunt. Cras dapibus. Vivamus elementum semper nisi. Aenean vulputate eleifend tellus. Aenean leo ligula, porttitor eu,</p>
    <h4>DONEC PEDE JUSTO, FRINGILLA VEL?</h4>
    <p>aliquet nec, vulputate eget, arcu. In enim justo, rhoncus ut, imperdiet a, venenatis vitae, justo. Nullam dictum felis eu pede mollis pretium. Integer tincidunt. Cras dapibus.</p>
  </div>
</section>

<section class="services">
  <div class="tab flip">OUR SERVICES</div>
  <div class="plans">
    <div class="plan">
      <div class="medal bronze" role="img" aria-label="Bronze medal graphic"></div>
      <h3>BRONZE<span class="kind">(SINGLE COACHING SESSION)</span></h3>
      <p>aliquet nec, vulputate eget, arcu.</p>
      <a class="order"><span class="order-icon"><svg width="18" height="22" viewBox="0 0 18 22"><path d="M6 2v11l-3-2-2 2 6 8h9V10l-7-2V2z" fill="#fff"/></svg></span>CLICK ORDER</a>
    </div>
    <div class="plan">
      <div class="medal silver" role="img" aria-label="Silver medal graphic"></div>
      <h3>SILVER<span class="kind">(SMALL-PACKAGE)</span></h3>
      <p>aliquet nec, vulputate eget, arcu.</p>
      <a class="order"><span class="order-icon"><svg width="18" height="22" viewBox="0 0 18 22"><path d="M6 2v11l-3-2-2 2 6 8h9V10l-7-2V2z" fill="#fff"/></svg></span>CLICK ORDER</a>
    </div>
    <div class="plan">
      <div class="medal gold" role="img" aria-label="Gold medal graphic"></div>
      <h3>GOLD<span class="kind">(LARGE-PACKAGE)</span></h3>
      <p>aliquet nec, vulputate eget, arcu.</p>
      <a class="order"><span class="order-icon"><svg width="18" height="22" viewBox="0 0 18 22"><path d="M6 2v11l-3-2-2 2 6 8h9V10l-7-2V2z" fill="#fff"/></svg></span>CLICK ORDER</a>
    </div>
  </div>
  <p class="guarantee">Money- Back Guarantee: If you are not satisfied , please contact us within 14 days after the first coaching call, so you get the money back .</p>
</section>

<section class="testimonials">
  <div class="tab flip">TESTIMONIALS</div>
  <p class="quote">"Uppiggande och inspirerande! Kommer med enkla vardagstips såväl som svårare tips. Ett roligt sätt att få en spark i baken, så att ekonomi-energin bibehålls! Tack för ett bra samtal!" - HENRIETTA BJURVIK</p>
</section>

<section class="coaches">
  <div class="tab flip">WE AS COACHES</div>
  <div class="coach" style="left:220px">
    <div class="coach-photo" role="img" aria-label="Portrait photo of coach Torbjörn Lindqvar"></div>
    <h3>TORBJÖRN LINDQVAR</h3>
    <div class="mail">torbjorn@kolmsteg.se</div>
    <p>Lorem ipsum dolor sit amet, consectetuer adipiscing elit. Aenean commodo ligula eget dolor. Aenean massa. Cum sociis natoque penatibus et</p>
  </div>
  <div class="divider"></div>
  <div class="coach" style="left:683px">
    <div class="coach-photo" role="img" aria-label="Portrait photo of coach Rasmus Tellvik"></div>
    <h3>RASMUS TELLVIK</h3>
    <div class="mail">rasmus@kolmsteg.se</div>
    <p>Lorem ipsum dolor sit amet, consectetuer adipiscing elit. Aenean commodo ligula eget dolor. Aenean massa. Cum sociis natoque penatibus et</p>
  </div>
</section>

<footer class="footer">
  <div class="tab flip">REACH US AT:</div>
  <div class="contact">
    <p>Contact Us:</p>
    <p class="gap">Kolm Steg AB<br>Ekbackevägen 12<br>412 60 Sundholm</p>
    <p class="gap">Vid frågor kontakta oss på team@kolmsteg.se</p>
  </div>
  <div class="follow">Follow us on:</div>
  <div class="social" style="top:40px"><span class="dot"></span>Flödet</div>
  <div class="social" style="top:106px"><span class="dot"></span>Kvittra</div>
  <div class="copyright">Copyright 2016 Kolm Steg AB</div>
</footer>

</body>
</html>
```